Flyer-Design für Fellglück Service
Zielgruppe
Fellglück Service bietet Haustierbetreuung in Nürnberg und Fürth an. Betreut werden Hunde, Katzen und Kleintiere. Die Zielgruppe ist also 18+ Jahre mit einen Haustier, dass betreut werden soll. Die Hauptzielgruppe sind Hundebesitzer die Tagesbetreuung oder Gassi-Service suchen.
Aufgabenstellung
Formate bitte alle üblichen Flyer Größen. Wer Fleißig ist macht auch Vorschläge für eine Broschüre. Wer eine gute Idee hat für einen Gutschein, kann diesen mit einbauen. Der angehängte Flyer wurde von mir selbst gestaltet, also bitte nich wundern, ob der unprofessionalität.
Mehr Input findet Ihr auf www.fellglueck-service.de oder auf der Facebook Seite Fellglück Service.
Den Flyer bitte beidseitig konziieren.

```html
<!DOCTYPE html>
<html lang="de">
<head>
<meta charset="utf-8">
<title>Fellglück Service – Flyer A6</title>
<link href="https://fonts.googleapis.com/css2?family=Archivo+Black&family=Arimo:wght@400;700&display=swap" rel="stylesheet">
<style>
  :root{
    --bg:#a9a8a4;
    --paper:#ffffff;
    --green:#9ca653;
    --ink-light:#ffffff;
    --water:#7c97b8;
    --fur:#6b4a35;
    --cat:#8a8a86;
    --garden:#6f8a4a;
    --grass:#4f7a2c;
  }
  html,body{margin:0;padding:0;width:1200px;height:1200px;overflow:hidden;}
  body{background:var(--bg);font-family:"Arimo",Arial,sans-serif;position:relative;}
  .flyer{position:absolute;top:232px;width:520px;height:736px;background:var(--paper);box-shadow:0 4px 14px rgba(0,0,0,.25);}
  .flyer--front{left:50px;}
  .flyer--back{left:630px;}
  .photo{position:absolute;}
  .headline{font-family:"Archivo Black",Arial,sans-serif;color:var(--ink-light);line-height:.98;margin:0;font-weight:400;}

  /* front */
  .photo--dogs{left:22px;top:22px;width:476px;height:388px;
    background:linear-gradient(160deg,#9fb4cf 0%,var(--water) 45%,var(--fur) 70%,#3a3a3a 100%);}
  .front-title{position:absolute;left:28px;top:288px;font-size:50px;}
  .photo--cat{left:22px;top:420px;width:168px;height:294px;
    background:linear-gradient(180deg,#6e6e6a,var(--cat) 50%,#b0b0aa);}
  .photo--child{left:200px;top:420px;width:298px;height:180px;
    background:linear-gradient(135deg,#4e7036,var(--garden) 45%,#e7c9d2 80%,#f2f2f2);}
  .tagline-band{position:absolute;left:200px;top:610px;width:298px;height:104px;background:var(--green);}
  .tagline{position:absolute;left:10px;bottom:10px;margin:0;color:var(--ink-light);font-weight:700;font-size:15px;}

  /* back */
  .info-block{position:absolute;left:22px;top:22px;width:476px;height:433px;background:var(--green);color:var(--ink-light);}
  .back-title{font-size:48px;margin:6px 0 0 4px;}
  .intro{font-size:14.5px;line-height:1.3;margin:18px 16px 6px 12px;}
  .services-head{font-weight:700;font-size:14.5px;margin:0 12px;}
  .services{margin:0 12px;padding:0 0 0 32px;font-size:14.5px;line-height:1.28;}
  .cta{font-size:14.5px;line-height:1.3;margin:8px 12px 0;}
  .contact{position:absolute;left:0;right:0;top:330px;display:flex;font-size:14px;line-height:1.32;}
  .contact__brand{width:200px;text-align:right;padding-right:26px;}
  .contact__brand strong{display:block;}
  .contact__details{flex:1;}
  .photo--guineapig{left:22px;top:465px;width:476px;height:249px;
    background:linear-gradient(120deg,var(--grass) 0%,#6d9a3a 45%,#d8c9a2 65%,#3b3a2c 100%);}
  .voucher{position:absolute;left:186px;top:598px;width:316px;height:120px;background:var(--paper);}
  .voucher__inner{position:absolute;left:6px;top:6px;right:6px;bottom:6px;background:var(--green);color:var(--ink-light);padding:6px 10px;box-sizing:border-box;}
  .voucher__title{font-weight:700;font-size:16px;margin:0;}
  .voucher__text{font-size:14px;line-height:1.2;margin:2px 0 6px;}
  .voucher__note{font-size:9px;margin:0;}
</style>
</head>
<body>
  <section class="flyer flyer--front">
    <div class="photo photo--dogs" role="img" aria-label="Foto: zwei Hunde rennen durch spritzendes Wasser, einer trägt einen Stock"></div>
    <h1 class="headline front-title">Fellglück<br>Service</h1>
    <div class="photo photo--cat" role="img" aria-label="Foto: getigerte Katze putzt ihre Pfote"></div>
    <div class="photo photo--child" role="img" aria-label="Foto: Mädchen mit weißem Kaninchen im Garten"></div>
    <div class="tagline-band"><p class="tagline">Ihre Haustierbetreuung</p></div>
  </section>

  <section class="flyer flyer--back">
    <div class="info-block">
      <h2 class="headline back-title">Fellglück<br>Service</h2>
      <p class="intro">Sie benötigen eine erfahrene und professionelle Betreuung für Ihr Haustier? Dann bin ich für Sie da!</p>
      <p class="services-head">Meine Dienstleistungen für Sie sind:</p>
      <ul class="services">
        <li>Gassiservice für Hunde</li>
        <li>Betreuung Ihres Haustieres bei Ihnen vor Ort</li>
        <li>Betreuung Ihres Haustieres bei mir</li>
      </ul>
      <p class="cta">Nutzen Sie gleich eine der vielen Kontaktmöglichkeiten und reservieren Sie Ihre Betreuung bei mir!</p>
      <div class="contact">
        <div class="contact__brand"><strong>Fellglück Service</strong>Eine liebevolle Betreuung für Ihr Haustier!</div>
        <div class="contact__details">www.fellglueck-service.de<br>Tel.: +49 0911 555 2741<br>email: kontakt@fellglueck-service.de</div>
      </div>
    </div>
    <div class="photo photo--guineapig" role="img" aria-label="Foto: Meerschweinchen auf dem Rasen vor einer Baumwurzel"></div>
    <div class="voucher">
      <div class="voucher__inner">
        <p class="voucher__title">Gutschein</p>
        <p class="voucher__text">für einen gratis Kennenlern-Termin mit Ihrem Haustier!</p>
        <p class="voucher__note">*nur gültig, falls eine Betreuung für mich möglich und relevant ist</p>
      </div>
    </div>
  </section>
</body>
</html>
```